Book cover design for my new Bankruptcy Law Book

Hi

I would like to get a unique and nice design for my new book titled: "Insolvency Framework Under Omani Trade Code".

I like blue color. It will be in Arabic so I care the most about the design of the book cover and not the words on the cover as the printing company will handle the rest.

Much appreciated,

SAEED AL-MARZOUQ

Colors
0692cd
33a6d7
86cae7
85abd2
3277b5
0255a3

Requirements
Must have
• Blue color
Nice to have
• pictures or shapes related to bankruptcy or insolvency

```html
<!DOCTYPE html>
<html lang="ar">
<head>
<meta charset="utf-8">
<title>Insolvency Framework Under Omani Trade Code — Book Cover</title>
<link rel="stylesheet" href="https://fonts.googleapis.com/css2?family=Amiri:wght@400;700&family=Questrial&display=swap">
<style>
  :root {
    --stage: #e9eef4;
    --navy-top: #1a2658;
    --navy-mid: #121b47;
    --navy-deep: #080d2c;
    --spine: #141d4c;
    --band-navy: #10173f;
    --gold: #cdbd8d;
    --gold-light: #e2d6aa;
    --gold-dark: #9b8352;
    --ornament-gold: #b89a55;
    --text-light: #ffffff;
    --photo-grey: #5c5c5c;
  }
  * { margin: 0; padding: 0; box-sizing: border-box; }
  html, body {
    width: 1200px; height: 875px; overflow: hidden;
    background: var(--stage);
  }
  .cover {
    position: absolute; left: 97px; top: 132px;
    width: 1006px; height: 611px;
    background: linear-gradient(180deg, var(--navy-top) 0%, var(--navy-mid) 45%, var(--navy-deep) 90%);
    overflow: hidden;
  }
  .pattern {
    position: absolute;
    background: linear-gradient(180deg, rgba(40,56,120,0.35), rgba(20,28,70,0.15));
  }
  .back-cover { position: absolute; left: 0; top: 0; width: 475px; height: 545px; }
  .back-cover .pattern { inset: 0; }
  .back-title {
    position: absolute; left: 0; width: 470px; top: 40px; text-align: center;
    font-family: "Amiri", serif; font-weight: 700; color: var(--gold);
    font-size: 40px; line-height: 1;
  }
  .back-subtitle {
    position: absolute; left: 0; width: 470px; top: 86px; text-align: center;
    font-family: "Amiri", serif; color: var(--gold); font-size: 21px; line-height: 1.2;
  }
  .description {
    position: absolute; left: 30px; width: 410px; top: 148px; text-align: center;
    font-family: "Questrial", sans-serif; color: var(--text-light);
    font-size: 13.5px; line-height: 17px;
  }
  .description h2 { font-weight: 400; font-size: 14px; }
  .author-photo {
    position: absolute; left: 52px; top: 369px; width: 88px; height: 103px;
    background: var(--photo-grey);
    display: flex; align-items: center; justify-content: center; text-align: center;
    font-family: "Questrial", sans-serif; font-style: italic; color: var(--text-light);
    font-size: 13px; line-height: 15px;
  }
  .author-bio {
    position: absolute; left: 158px; top: 369px; width: 265px;
    font-family: "Questrial", sans-serif; color: var(--text-light);
    font-size: 12px; line-height: 16px;
  }
  .author-bio strong { font-weight: 700; }

  .spine {
    position: absolute; left: 475px; top: 0; width: 59px; height: 545px;
    background: linear-gradient(90deg, #0b1132 0%, var(--spine) 18%, var(--spine) 82%, #0b1132 100%);
  }
  .spine-text {
    position: absolute; left: 0; width: 59px;
    writing-mode: vertical-rl;
    font-family: "Amiri", serif; color: var(--text-light);
    display: flex; align-items: center; justify-content: center;
  }
  .spine-author { top: 48px; height: 150px; font-size: 21px; color: var(--gold-light); font-weight: 700; }
  .spine-subtitle { top: 272px; height: 120px; font-size: 13px; line-height: 17px; }
  .spine-title { top: 405px; height: 95px; font-size: 34px; font-weight: 700; }

  .front-cover { position: absolute; left: 534px; top: 0; width: 472px; height: 545px; }
  .front-cover .pattern.top { left: 0; top: 0; width: 472px; height: 103px; }
  .front-cover .pattern.bottom { left: 0; top: 291px; width: 472px; height: 254px; }
  .title-band {
    position: absolute; left: 0; top: 103px; width: 472px; height: 188px;
    background: var(--band-navy);
  }
  .ornament-rule {
    position: absolute; left: 0; width: 472px; height: 12px;
    background: linear-gradient(180deg, transparent 0 3px, var(--ornament-gold) 3px 9px, transparent 9px);
    opacity: 0.85;
  }
  .ornament-rule.upper { top: 103px; }
  .ornament-rule.lower { top: 279px; }
  .front-title {
    position: absolute; left: 0; width: 472px; top: 150px; text-align: center;
    font-family: "Amiri", serif; font-weight: 700; color: var(--gold);
    font-size: 54px; line-height: 1;
  }
  .front-subtitle {
    position: absolute; left: 0; width: 472px; top: 212px; text-align: center;
    font-family: "Amiri", serif; color: var(--gold-light); font-size: 29px; line-height: 1.2;
  }
  .front-author {
    position: absolute; left: 0; width: 472px; top: 332px; text-align: center;
    font-family: "Amiri", serif; font-weight: 700; color: var(--gold); font-size: 30px;
  }

  .gold-rule {
    position: absolute; left: 0; top: 545px; width: 1006px; height: 3px;
    background: linear-gradient(90deg, var(--gold-dark), var(--gold-light), var(--gold-dark), var(--gold-light), var(--gold-dark));
  }
  .gold-band {
    position: absolute; left: 0; top: 558px; width: 1006px; height: 53px;
    background: linear-gradient(90deg, #8f7748 0%, #c9bb91 22%, #a48b5a 40%, #8f7748 50%, #cfc29a 75%, #9a8150 100%);
  }
</style>
</head>
<body>
  <main class="cover">
    <section class="back-cover">
      <div class="pattern" role="img" aria-label="Faint geometric Arabesque pattern in navy"></div>
      <h1 class="back-title" lang="ar">إعسار</h1>
      <p class="back-subtitle" lang="ar">الإطار في ضوء قانون التجارة العُماني</p>
      <div class="description" lang="en">
        <h2>BOOK DESCRIPTION</h2>
        <p>Lorem ipsum text content goes here.. lorem ipsum text content goes here.. lorem ipsum text content goes here..</p>
      </div>
      <div class="author-photo" lang="en">AUTHOR'S<br>PICTURE</div>
      <p class="author-bio" lang="en"><strong>AUTHOR NAME</strong> Lorem ipsum text content goes here.. Lorem ipsum text content goes here..</p>
    </section>

    <section class="spine">
      <span class="spine-text spine-author" lang="ar">سعيد المرزوق</span>
      <span class="spine-text spine-subtitle" lang="ar">الإطار في ضوء<br>قانون التجارة العُماني</span>
      <span class="spine-text spine-title" lang="ar">إعسار</span>
    </section>

    <section class="front-cover">
      <div class="pattern top" role="img" aria-label="Geometric Arabesque star pattern in navy"></div>
      <div class="title-band"></div>
      <div class="ornament-rule upper" role="img" aria-label="Gold braided ornamental border"></div>
      <div class="ornament-rule lower" role="img" aria-label="Gold braided ornamental border"></div>
      <h1 class="front-title" lang="ar">إعسار</h1>
      <p class="front-subtitle" lang="ar">الإطار في ضوء قانون التجارة العُماني</p>
      <div class="pattern bottom" role="img" aria-label="Geometric Arabesque star pattern in navy"></div>
      <p class="front-author" lang="ar">سعيد المرزوق</p>
    </section>

    <div class="gold-rule"></div>
    <div class="gold-band"></div>
  </main>
</body>
</html>
```